Business cards - KESTO Roofing & Siding

We need simple business cards made up for our Roofing & Siding business based in Calgary Alberta.
The logo on one side of the card and potentially our slogan "Built with trust, verified by time".
The other side could have:
-A small logo
-Rep name:
-Rep cell phone:
-Rep email:
-Office phone: 403-386-2049
-Website: PrairieShinglePros.com

We would like to incorporate the colours from our logo, especially the lite blue on the jpeg file. I have attached the ai file and jpeg file. We like the colours better on the jpeg file.

I do not require a money back guarantee

```html
<!DOCTYPE html>
<html lang="en">
<head>
<meta charset="utf-8">
<title>KESTO Roofing &amp; Siding — Business Cards</title>
<link rel="stylesheet" href="https://fonts.googleapis.com/css2?family=Lato:wght@300;400;700;900&display=swap">
<style>
  :root {
    --backdrop: #2c2c2c;
    --card: #ffffff;
    --band-blue: #4a89c8;
    --icon-blue: #1667b5;
    --ink: #111111;
    --ink-soft: #2a2a2a;
  }
  * { box-sizing: border-box; margin: 0; padding: 0; }
  html, body {
    width: 1200px; height: 1200px; overflow: hidden;
    background: var(--backdrop);
    font-family: "Lato", sans-serif;
  }
  .canvas { position: relative; width: 1200px; height: 1200px; }
  .card {
    position: absolute; left: 239px; width: 722px; height: 412px;
    background: var(--card); border-radius: 20px; overflow: hidden;
  }
  .card--front { top: 140px; }
  .card--back { top: 645px; }
  .bands { position: absolute; inset: 0; width: 722px; height: 412px; }
  .bands polygon { fill: var(--band-blue); }

  .brand-small {
    position: absolute; left: 58px; top: 62px;
    display: flex; align-items: center; gap: 12px;
    color: var(--ink); font-weight: 900;
  }
  .brand-small .brand-mark { width: 26px; height: 26px; background: var(--icon-blue); }
  .brand-small .brand-name { font-size: 30px; letter-spacing: 1px; line-height: 1; }
  .brand-small .brand-sub { font-size: 15px; letter-spacing: 3px; line-height: 1; margin-top: 6px; text-transform: uppercase; }

  .rep-name {
    position: absolute; left: 51px; top: 194px;
    font-size: 38px; font-weight: 900; color: var(--ink); letter-spacing: 0.3px;
  }
  .rep-title {
    position: absolute; left: 52px; top: 236px;
    font-size: 20px; font-weight: 400; color: var(--band-blue);
  }
  .contact { position: absolute; display: flex; align-items: center; gap: 11px;
    font-size: 21px; font-weight: 300; color: var(--ink-soft); }
  .contact svg { width: 25px; height: 25px; flex: none; }
  .contact--cell { left: 50px; top: 297px; }
  .contact--office { left: 50px; top: 334px; }
  .contact--email { left: 289px; top: 297px; }
  .contact--web { left: 289px; top: 334px; }

  .brand-large {
    position: absolute; right: 48px; bottom: 46px; text-align: right;
    display: flex; align-items: center; gap: 18px;
    color: var(--ink); font-weight: 900;
  }
  .brand-large .brand-mark { width: 44px; height: 44px; background: var(--icon-blue); }
  .brand-large .brand-name { font-size: 86px; line-height: 0.9; letter-spacing: 4px; }
  .brand-large .brand-sub { font-size: 26px; letter-spacing: 6px; text-transform: uppercase; margin-top: 10px; }
</style>
</head>
<body>
<main class="canvas">

  <section class="card card--front" aria-label="Card front">
    <svg class="bands" viewBox="0 0 722 412" aria-hidden="true">
      <polygon points="362,0 550,0 722,179 722,376"/>
      <polygon points="617,0 722,0 722,109"/>
    </svg>

    <div class="brand-small">
      <span class="brand-mark"></span>
      <div>
        <div class="brand-name">KESTO</div>
        <div class="brand-sub">Roofing &amp; Siding</div>
      </div>
    </div>

    <h1 class="rep-name">YOUR NAMEHERE</h1>
    <p class="rep-title">Designation</p>

    <div class="contact contact--cell">
      <svg viewBox="0 0 24 24" aria-hidden="true"><circle cx="12" cy="12" r="12" fill="var(--icon-blue)"/><path d="M9 6.5l1.6 2.6-1.1 1.2c.6 1.6 1.6 2.7 3.2 3.4l1.2-1.1 2.6 1.6-.9 2c-4.6-.2-8.2-3.8-8.4-8.5z" fill="#fff"/></svg>
      <span>000-123-4567</span>
    </div>
    <div class="contact contact--office">
      <svg viewBox="0 0 24 24" aria-hidden="true"><circle cx="12" cy="12" r="12" fill="var(--icon-blue)"/><path d="M9 6.5l1.6 2.6-1.1 1.2c.6 1.6 1.6 2.7 3.2 3.4l1.2-1.1 2.6 1.6-.9 2c-4.6-.2-8.2-3.8-8.4-8.5z" fill="#fff"/></svg>
      <span>403-386-2049</span>
    </div>
    <div class="contact contact--email">
      <svg viewBox="0 0 24 24" aria-hidden="true"><circle cx="12" cy="12" r="12" fill="var(--icon-blue)"/><rect x="6.5" y="8" width="11" height="8" rx="1" fill="none" stroke="#fff" stroke-width="1.6"/><path d="M6.8 8.5l5.2 4 5.2-4" fill="none" stroke="#fff" stroke-width="1.6"/></svg>
      <span>your@email.email</span>
    </div>
    <div class="contact contact--web">
      <svg viewBox="0 0 24 24" aria-hidden="true"><circle cx="12" cy="12" r="11" fill="none" stroke="var(--icon-blue)" stroke-width="2"/><ellipse cx="12" cy="12" rx="4.5" ry="11" fill="none" stroke="var(--icon-blue)" stroke-width="2"/><path d="M1 12h22M3 6.5h18M3 17.5h18M12 1v22" stroke="var(--icon-blue)" stroke-width="2"/></svg>
      <span>PrairieShinglePros.com</span>
    </div>
  </section>

  <section class="card card--back" aria-label="Card back">
    <svg class="bands" viewBox="0 0 722 412" aria-hidden="true">
      <polygon points="0,0 107,0 0,112"/>
      <polygon points="175,0 362,0 0,379 0,182"/>
    </svg>

    <div class="brand-large">
      <span class="brand-mark"></span>
      <div>
        <div class="brand-name">KESTO</div>
        <div class="brand-sub">Roofing &amp; Siding</div>
      </div>
    </div>
  </section>

</main>
</body>
</html>
```